Kestrel Property Management email template

Looking for an email template for communications sent to residents that reads well in most email formats including mobile devices. Similar to the attached email, not quite reclaimed wood but something warm with interesting texture

```html
<!DOCTYPE html>
<html lang="en">
<head>
<meta charset="utf-8">
<title>Kestrel Property Management – Resident Newsletter</title>
<link rel="stylesheet" href="https://fonts.googleapis.com/css2?family=Crimson+Pro:wght@600&family=Montserrat:wght@400;500;600&family=Open+Sans:wght@600&display=swap">
<style>
  :root {
    --navy: #131f4a;
    --blue: #345ea3;
    --nav-link: #7096d2;
    --heading-blue: #3a5fa0;
    --pale: #e1eaf5;
    --body-text: #55565a;
    --white: #ffffff;
    --warm-1: #e3b25e;
    --warm-2: #f0cd86;
    --warm-3: #c99446;
    --social-1: #5477c1;
    --social-2: #74c6ee;
    --social-3: #c9192c;
  }
  * { margin: 0; padding: 0; box-sizing: border-box; }
  html, body { width: 1200px; height: 2798px; overflow: hidden; background: var(--white); }
  body { font-family: "Montserrat", Arial, sans-serif; position: relative; }

  .preheader {
    height: 75px; background: var(--pale);
    display: flex; align-items: center; justify-content: center;
    font-family: Arial, Helvetica, sans-serif; font-size: 21px; color: var(--navy);
  }
  .backdrop {
    position: absolute; left: 0; top: 75px; width: 1200px; height: 2178px;
    background:
      radial-gradient(ellipse 260px 500px at 60px 1900px, rgba(185,120,40,.45), transparent 70%),
      radial-gradient(ellipse 300px 600px at 1150px 500px, rgba(250,220,160,.6), transparent 70%),
      radial-gradient(ellipse 200px 400px at 80px 700px, rgba(200,140,60,.35), transparent 70%),
      linear-gradient(90deg, var(--warm-3) 0%, var(--warm-1) 6%, var(--warm-2) 12%, var(--warm-1) 88%, var(--warm-2) 94%, var(--warm-1) 100%);
  }
  .email {
    position: absolute; left: 150px; top: 75px; width: 900px; height: 2178px;
    background: var(--white);
  }
  .brand {
    height: 314px; display: flex; align-items: center; justify-content: center; gap: 18px;
  }
  .brand-square { width: 30px; height: 30px; background: var(--navy); }
  .brand-name {
    font-family: "Montserrat", Arial, sans-serif; font-weight: 500;
    font-size: 40px; color: var(--navy); letter-spacing: 1px;
  }
  .nav {
    height: 90px; background: var(--navy);
    display: flex; align-items: center; justify-content: center; gap: 42px;
    font-size: 26px; font-weight: 500;
  }
  .nav a { color: var(--nav-link); text-decoration: none; }
  .nav a.is-current { color: var(--white); }
  .hero {
    position: relative; height: 574px;
    background:
      linear-gradient(180deg, #b9a47a 0%, #8f7a55 28%, #dcdad4 45%, #e6e4df 70%, #9c8a63 100%);
  }
  .hero-notch { position: absolute; left: 402px; bottom: 0; }
  .intro { text-align: center; padding-top: 50px; }
  .intro-title {
    font-family: "Crimson Pro", "Palatino Linotype", serif; font-weight: 600;
    font-size: 56px; color: var(--navy); line-height: 1.1;
  }
  .intro-slogan {
    font-family: Arial, Helvetica, sans-serif; font-size: 26px; color: #3b3f55; margin-top: 8px;
  }
  .intro-copy {
    margin: 44px auto 0; width: 830px; font-size: 21.5px; line-height: 30px; color: var(--body-text);
  }
  .intro-copy p + p { margin-top: 30px; }
  .section-heading {
    margin: 72px auto 0; width: 214px; text-align: center;
    font-family: "Crimson Pro", "Palatino Linotype", serif; font-weight: 600;
    font-size: 38px; color: var(--heading-blue); line-height: 1;
    padding-bottom: 18px; border-bottom: 5px solid var(--heading-blue);
  }
  .features { list-style: none; margin: 70px 0 0 166px; }
  .features li {
    display: flex; align-items: center; gap: 30px; height: 54px;
    font-size: 22px; color: var(--body-text);
  }
  .features li::before {
    content: ""; width: 14px; height: 14px; background: var(--blue); flex: none;
  }
  .cta {
    display: flex; align-items: center; justify-content: center;
    width: 614px; height: 77px; margin: 96px auto 0;
    background: var(--blue); color: var(--white); text-decoration: none;
    font-size: 29px; font-weight: 600; letter-spacing: 5px;
  }
  .footer {
    position: absolute; left: 0; top: 2253px; width: 1200px; height: 361px;
    background: var(--navy); color: var(--white); text-align: center;
  }
  .footer-brand {
    display: flex; align-items: center; justify-content: center; gap: 22px; height: 190px;
  }
  .footer-brand .brand-square { background: var(--white); width: 34px; height: 34px; }
  .footer-brand-name {
    font-family: "Open Sans", Arial, sans-serif; font-weight: 600; font-size: 27px;
  }
  .footer-contact { font-size: 23px; line-height: 52px; }
  .footer-contact strong { font-weight: 600; }
  .footer-contact .sep { margin: 0 18px; }
  .social {
    position: absolute; top: 2660px; left: 0; width: 1200px;
    display: flex; justify-content: center; gap: 8px;
  }
  .social span { width: 75px; height: 75px; border-radius: 50%; display: block; }
  .social .s1 { background: var(--social-1); }
  .social .s2 { background: var(--social-2); }
  .social .s3 { background: var(--social-3); }
</style>
</head>
<body>
  <div class="preheader">Don’t see this email properly? View in web browser</div>
  <div class="backdrop" role="img" aria-label="Warm aged parchment texture in golden tones"></div>

  <main class="email">
    <header class="brand">
      <span class="brand-square"></span>
      <span class="brand-name">Kestrel Property Management</span>
    </header>

    <nav class="nav">
      <a href="#" class="is-current">HOME</a>
      <a href="#">ABOUT</a>
      <a href="#">SERVICES</a>
      <a href="#">CONTACT</a>
    </nav>

    <div class="hero" role="img" aria-label="Photo of a white clapboard house with red trim, a picket fence and an autumn tree">
      <svg class="hero-notch" width="96" height="48" viewBox="0 0 96 48"><polygon points="0,48 48,0 96,48" fill="#ffffff"/></svg>
    </div>

    <section class="intro">
      <h1 class="intro-title">Lorel Ipsum Dolor Sit Amet</h1>
      <p class="intro-slogan">sub heading/slogan goes her</p>
      <div class="intro-copy">
        <p>Nam eget justo porttitor, dictum eros quis, lobortis lacus. Donec malesuada libero sit amet ultricies vestibulum. Nulla sed risus id elit tempus tempus ac et nibh. Curabitur dolor risus, hendrerit vitae nunc eu, fringilla porta orci. Pellen­tesque congue eu sem eget venenatis.</p>
        <p>Nullam sem diam, dignissim non faucibus molestie, placerat eget nisi. Etiam eget ultricies nisi. Donec bibendum enim in ex blandit pulvinar. Nulla cursus eu nunc sed tempus. Sed placerat sodales metus quis venenatis. Aenean et velit vitae leo facilisis tristique.</p>
      </div>
      <h2 class="section-heading">Sub Heading</h2>
    </section>

    <ul class="features">
      <li>In viverra ipsum a lectus convallis porttitor.</li>
      <li>Donec id diam et quam commodo tristique.</li>
      <li>Aliquam porta nisi a porttitor porta.</li>
      <li>Etiam id nisi sagittis lorem facilisis condimentum.</li>
    </ul>

    <a href="#" class="cta">CALL TO ACTION</a>
  </main>

  <footer class="footer">
    <div class="footer-brand">
      <span class="brand-square"></span>
      <span class="footer-brand-name">KESTREL PROPERTY MANAGEMENT</span>
    </div>
    <p class="footer-contact"><strong>Phone:</strong> 555 .0142.7390<span class="sep">|</span><strong>Email:</strong> hello@kestrelpm-mail.com</p>
    <p class="footer-contact">Larkspur Lane 48, 5017 Maple Ridge, USA</p>
  </footer>

  <div class="social">
    <span class="s1" role="img" aria-label="Social link"></span>
    <span class="s2" role="img" aria-label="Social link"></span>
    <span class="s3" role="img" aria-label="Video channel link"></span>
  </div>
</body>
</html>
```